Mobile digital movie retailer needs design for rewards program app

We would like designs for an 1-page Android app that allows users to rent new release movies and promotes loyalty through a rewards program. The rewards program should have 5-6 tiers -- users earn points for each movie they rent. Users in higher tiers get special offers like free rentals and early access to upcoming titles.
We only offer 5-10 movies at a single time, so there's no need for a sorting or filtering. A simple list will do.
The designs should communicate the following: user's current tier, how close the user is to achieving the next tier, # of movies the user has purchased (and other relevant stats).

```html
<!DOCTYPE html>
<html lang="en">
<head>
<meta charset="utf-8">
<title>FlickWarden – Rewards App</title>
<link href="https://fonts.googleapis.com/css2?family=Cabin:ital,wght@0,400;0,600;0,700;1,400;1,600&display=swap" rel="stylesheet">
<style>
  :root {
    --brand-red: #e2502a;
    --deep-red: #b8361c;
    --gold: #e5a42b;
    --gold-dark: #c98a1b;
    --peach: #f7c2a0;
    --white: #ffffff;
    --ink-red: #d8431f;
    --muted-red: #c2502e;
    --button-gold-top: #e8b04a;
    --button-gold-bottom: #a9741a;
    --button-red-top: #ee5a34;
    --button-red-bottom: #a82c13;
  }
  * { box-sizing: border-box; margin: 0; padding: 0; }
  html, body { width: 1200px; height: 1000px; overflow: hidden; background: var(--white); }
  body { position: relative; font-family: "Cabin", sans-serif; color: var(--white); }

  /* Brand block */
  .brand { position: absolute; left: 450px; top: 70px; width: 300px; text-align: center; }
  .brand-mark { width: 150px; height: 150px; border-radius: 50%; background: var(--brand-red); margin: 40px auto 40px; }
  .brand-name { font-size: 27px; font-weight: 700; color: var(--brand-red); line-height: 1; }
  .brand-tagline { font-size: 19px; font-style: italic; color: var(--brand-red); margin-top: 4px; }
  .brand-tagline strong { font-weight: 700; }

  /* Rank legend */
  .ranks { position: absolute; left: 455px; top: 400px; width: 290px; text-align: center; }
  .ranks-title { font-size: 18px; font-weight: 700; color: var(--brand-red); line-height: 1.1; }
  .rank-grid { display: grid; grid-template-columns: 145px 145px; row-gap: 42px; margin-top: 14px; }
  .rank { display: flex; flex-direction: column; align-items: center; }
  .rank-badge { width: 62px; height: 62px; border-radius: 50%; background: var(--brand-red); border: 4px solid var(--gold); margin: 10px 0 14px; }
  .rank-name { font-size: 12.5px; font-weight: 700; color: var(--ink-red); }

  /* App screens */
  .screen { position: absolute; top: 415px; width: 224px; height: 428px; overflow: hidden; background: var(--gold); }
  .screen--home { left: 159px; }
  .screen--rankup { left: 783px; width: 242px; }
  .app-bar { height: 40px; background: var(--brand-red); display: flex; align-items: center; padding: 0 12px 0 20px; }
  .app-title { font-size: 17px; font-weight: 700; flex: 1; }
  .app-icons { display: flex; align-items: center; gap: 14px; font-weight: 700; font-size: 17px; }
  .app-icons svg { display: block; }

  /* Home: rank status */
  .status { height: 143px; background: var(--gold); text-align: center; padding-top: 14px; }
  .status-label { font-size: 10px; font-weight: 600; }
  .status-rank { font-size: 21px; font-weight: 700; line-height: 1.05; }
  .progress { display: flex; align-items: center; justify-content: space-between; padding: 0 14px; margin-top: 8px; }
  .progress-badge { width: 26px; height: 26px; border-radius: 50%; background: var(--brand-red); border: 2px solid var(--gold-dark); flex: none; }
  .progress-track { flex: 1; height: 9px; margin: 0 2px; background: #d9872a; border-top: 2px solid var(--brand-red); border-bottom: 2px solid var(--brand-red); position: relative; }
  .progress-fill { position: absolute; left: 0; top: 0; bottom: 0; width: 25%; background: var(--deep-red); }
  .progress-note { font-size: 8.5px; font-style: italic; margin-top: -4px; }
  .progress-note b, .status-stats b { color: var(--deep-red); }
  .status-stats { font-size: 9px; font-weight: 600; line-height: 1.3; margin-top: 9px; padding: 0 18px; text-align: left; }

  /* Home: rentals */
  .rentals { height: 245px; background: linear-gradient(to bottom, var(--peach) 0%, var(--peach) 80%, var(--white) 100%); padding-top: 10px; }
  .rentals-title { font-size: 18px; font-weight: 700; text-align: center; margin: 0 20px; padding-bottom: 2px; border-bottom: 2px solid var(--white); }
  .rental-list { list-style: none; padding: 6px 0 0 20px; }
  .rental { display: flex; gap: 6px; height: 62px; }
  .rental-poster { width: 46px; height: 56px; background: var(--white); border: 1px solid #f0a67c; flex: none; }
  .rental-info { width: 150px; }
  .rental-title { font-size: 12px; font-weight: 700; color: var(--ink-red); line-height: 1.05; white-space: nowrap; }
  .rental-meta { font-size: 6.5px; font-style: italic; color: #9a5a3c; }
  .rental-history { font-size: 6.5px; color: var(--muted-red); }
  .rental-actions { display: flex; gap: 8px; margin-top: 3px; }
  .btn { height: 15px; font-size: 7px; display: flex; align-items: center; justify-content: center; border-radius: 1px; }
  .btn--info { width: 70px; font-style: italic; background: linear-gradient(var(--button-gold-top), var(--button-gold-bottom)); }
  .btn--rent { width: 70px; font-weight: 700; background: linear-gradient(var(--button-red-top), var(--button-red-bottom)); }

  /* Rank up */
  .rankup { text-align: center; padding-top: 10px; }
  .rankup-title { font-size: 34px; font-weight: 700; line-height: 1; text-shadow: 2px 2px 0 var(--deep-red); }
  .rankup-rule { height: 2px; background: var(--white); margin: 6px 16px 0; }
  .rankup-lead { font-size: 9px; font-weight: 600; margin-top: 8px; }
  .rankup-badge { width: 112px; height: 112px; border-radius: 50%; background: var(--brand-red); border: 5px solid var(--gold-dark); margin: 16px auto 12px; }
  .rankup-rank { font-size: 20px; font-weight: 700; text-shadow: 2px 2px 0 var(--deep-red); }
  .rankup-rank-rule { height: 2px; background: var(--white); margin: 2px 28px 0; }
  .rankup-perk { font-size: 9px; font-weight: 600; line-height: 1.3; margin: 12px 20px 0; }
  .rankup-code { font-size: 13px; font-weight: 700; margin-top: 10px; letter-spacing: 0.5px; }
  .btn--ok { width: 70px; height: 22px; margin: 18px auto 0; font-size: 14px; font-weight: 700; background: linear-gradient(var(--button-red-top), var(--button-red-bottom)); }
</style>
</head>
<body>

  <header class="brand">
    <div class="brand-mark"></div>
    <div class="brand-name">FlickWarden</div>
    <div class="brand-tagline">It’s an <strong>honor</strong> to watch!</div>
  </header>

  <section class="screen screen--home">
    <div class="app-bar">
      <span class="app-title">FlickWarden</span>
      <span class="app-icons">
        <svg width="17" height="17" viewBox="0 0 24 24" aria-hidden="true"><g fill="#fff"><circle cx="12" cy="12" r="7"/><rect x="10" y="1" width="4" height="22"/><rect x="1" y="10" width="22" height="4"/><rect x="10" y="1" width="4" height="22" transform="rotate(45 12 12)"/><rect x="10" y="1" width="4" height="22" transform="rotate(-45 12 12)"/></g><circle cx="12" cy="12" r="3" fill="#e2502a"/></svg>
        <span>?</span>
      </span>
    </div>

    <div class="status">
      <div class="status-label">Your Current Rank:</div>
      <div class="status-rank">MovieSquire</div>
      <div class="progress">
        <span class="progress-badge"></span>
        <span class="progress-track"><span class="progress-fill"></span></span>
        <span class="progress-badge"></span>
      </div>
      <div class="progress-note">XP needed for next rank: <b>112</b></div>
      <p class="status-stats">You have rented <b>10</b> different movies and gained a total of <b>138</b> XP. Outstanding!</p>
    </div>

    <div class="rentals">
      <h2 class="rentals-title">Current Rentals</h2>
      <ul class="rental-list">
        <li class="rental">
          <div class="rental-poster" role="img" aria-label="Movie poster"></div>
          <div class="rental-info">
            <div class="rental-title">That Movie with a Girl</div>
            <div class="rental-meta">(Chris Brocklin, 2084) (20 XP)</div>
            <div class="rental-history">You have <b>never</b> rented this movie before.</div>
            <div class="rental-actions"><span class="btn btn--info">More Information</span><span class="btn btn--rent">RENT for $19.99</span></div>
          </div>
        </li>
        <li class="rental">
          <div class="rental-poster" role="img" aria-label="Movie poster"></div>
          <div class="rental-info">
            <div class="rental-title">Titanic Revealed</div>
            <div class="rental-meta">(Harman Gusto, 2061) (40 XP)</div>
            <div class="rental-history">You have rented this movie <b>1</b> time. »</div>
            <div class="rental-actions"><span class="btn btn--info">More Information</span><span class="btn btn--rent">RENT AGAIN</span></div>
          </div>
        </li>
        <li class="rental">
          <div class="rental-poster" role="img" aria-label="Movie poster"></div>
          <div class="rental-info">
            <div class="rental-title">Ragnarok, MN</div>
            <div class="rental-meta">(Nora Fielding, 2033) (35 XP)</div>
            <div class="rental-history">You have rented this movie <b>5</b> times. »</div>
            <div class="rental-actions"><span class="btn btn--info">More Information</span><span class="btn btn--rent">RENT AGAIN</span></div>
          </div>
        </li>
      </ul>
    </div>
  </section>

  <section class="ranks">
    <h2 class="ranks-title">Rewards Program<br>Ranks</h2>
    <div class="rank-grid">
      <div class="rank"><span class="rank-badge"></span><span class="rank-name">MovieBeginner</span></div>
      <div class="rank"><span class="rank-badge"></span><span class="rank-name">MoviePage</span></div>
      <div class="rank"><span class="rank-badge"></span><span class="rank-name">MovieSquire</span></div>
      <div class="rank"><span class="rank-badge"></span><span class="rank-name">MovieKnight</span></div>
      <div class="rank"><span class="rank-badge"></span><span class="rank-name">MovieVanguard</span></div>
      <div class="rank"><span class="rank-badge"></span><span class="rank-name">FlickWarden</span></div>
    </div>
  </section>

  <section class="screen screen--rankup">
    <div class="app-bar">
      <span class="app-title">FlickWarden</span>
      <span class="app-icons">
        <svg width="17" height="17" viewBox="0 0 24 24" aria-hidden="true"><g fill="#fff"><circle cx="12" cy="12" r="7"/><rect x="10" y="1" width="4" height="22"/><rect x="1" y="10" width="22" height="4"/><rect x="10" y="1" width="4" height="22" transform="rotate(45 12 12)"/><rect x="10" y="1" width="4" height="22" transform="rotate(-45 12 12)"/></g><circle cx="12" cy="12" r="3" fill="#e2502a"/></svg>
        <span>?</span>
      </span>
    </div>
    <div class="rankup">
      <h1 class="rankup-title">Rank Up!</h1>
      <div class="rankup-rule"></div>
      <p class="rankup-lead">You have gained enough XP to become a</p>
      <div class="rankup-badge"></div>
      <div class="rankup-rank">MovieKnight</div>
      <div class="rankup-rank-rule"></div>
      <p class="rankup-perk">As a MovieKnight, you can now get free rentals* on up to 3 different titles per month. Simply enter the following code at checkout and enjoy!</p>
      <div class="rankup-code">MKNGTDSCT</div>
      <div class="btn btn--ok">OK</div>
    </div>
  </section>

</body>
</html>
```